Meridian Rest Supply Needs Business Card

Looking for a very nice looking business card. Creative but not extravagant. We sell beds and pillows across the U.S. and need something professional but catchy. I have attached the logo.

Name : Dale Fenwick
Title : President
Phone : (800) 417-2964
Email: sleep@quorvana.com
Website: www.quorvana.com

Can be single-sided or double-sided
horizontal or vertical

Can use Blues/Greys

Target Market(s)

Mass Market

Industry/Entity Type

Retail

Contact Information for Business Card

Name : Dale Fenwick
Title : President
Phone : (800) 417-2964
Email: sleep@quorvana.com
Website: www.quorvana.com

Requirements
Must have
• Clean, Modern, Smooth
• Can use Blues/Greys
• On the other side without the information - have something simple like www.quorvana.com or our logo
Nice to have
• Surprise me
Should not have
• Nothing crazy, nothing cluttered

```html
<!DOCTYPE html>
<html lang="en">
<head>
<meta charset="utf-8">
<title>Meridian Rest Supply – Business Card</title>
<link href="https://fonts.googleapis.com/css2?family=Roboto:wght@300;400;500;700&display=swap" rel="stylesheet">
<style>
  :root {
    --brand-blue: #33a2d4;
    --band-grey: #9a9a9a;
    --text-grey: #4a4a4a;
    --rule-grey: #dcdcdc;
    --card-white: #ffffff;
    --stage: #e9ebee;
  }
  * { margin: 0; padding: 0; box-sizing: border-box; }
  html, body {
    width: 1200px; height: 1000px; overflow: hidden;
    background: var(--stage);
    font-family: "Roboto", Arial, sans-serif;
  }
  .canvas { position: relative; width: 1200px; height: 1000px; }

  .card {
    position: absolute; left: 243px; width: 708px; height: 404px;
    box-shadow: 0 4px 14px rgba(0,0,0,0.12);
    overflow: hidden;
  }

  /* Front */
  .card-front { top: 84px; background: var(--brand-blue); color: var(--card-white); }
  .card-front .wordmark {
    position: absolute; left: 0; right: 0; top: 140px;
    text-align: center; font-weight: 300; font-size: 104px;
    letter-spacing: 2px; line-height: 1;
  }
  .card-front .website {
    position: absolute; left: 0; right: 0; top: 359px;
    text-align: center; font-size: 15px; font-weight: 400; letter-spacing: 0.3px;
  }

  /* Back */
  .card-back { top: 526px; background: var(--card-white); }
  .card-back .wordmark {
    position: absolute; right: 33px; top: 30px;
    color: var(--brand-blue); font-weight: 300; font-size: 60px;
    letter-spacing: 1.5px; line-height: 1;
  }
  .holder { position: absolute; left: 33px; top: 188px; }
  .holder-name {
    color: var(--brand-blue); font-weight: 700; font-size: 18px; letter-spacing: 0.3px;
  }
  .holder-title { color: var(--text-grey); font-size: 16px; margin-top: 2px; }
  .divider {
    position: absolute; left: 33px; right: 33px; top: 242px;
    height: 1px; background: var(--rule-grey);
  }
  .contacts { position: absolute; left: 33px; top: 258px; list-style: none; }
  .contacts li {
    display: flex; align-items: center; gap: 8px;
    color: var(--text-grey); font-size: 16px; height: 22.5px;
  }
  .contacts svg { width: 12px; height: 12px; fill: var(--brand-blue); flex: none; }
  .footer-band { position: absolute; left: 0; bottom: 0; width: 708px; height: 30px; }
</style>
</head>
<body>
<main class="canvas">
  <section class="card card-front" aria-label="Card front">
    <div class="wordmark">quorvana</div>
    <div class="website">www.quorvana.com</div>
  </section>

  <section class="card card-back" aria-label="Card back">
    <div class="wordmark">quorvana</div>
    <div class="holder">
      <div class="holder-name">DALE FENWICK</div>
      <div class="holder-title">President</div>
    </div>
    <div class="divider"></div>
    <ul class="contacts">
      <li>
        <svg viewBox="0 0 24 24" aria-hidden="true"><path d="M6.6 10.8a15.2 15.2 0 0 0 6.6 6.6l2.2-2.2a1 1 0 0 1 1-.25 11.4 11.4 0 0 0 3.6.57 1 1 0 0 1 1 1V20a1 1 0 0 1-1 1A17 17 0 0 1 3 4a1 1 0 0 1 1-1h3.5a1 1 0 0 1 1 1c0 1.25.2 2.45.57 3.57a1 1 0 0 1-.25 1z"/></svg>
        (800) 417-2964
      </li>
      <li>
        <svg viewBox="0 0 24 24" aria-hidden="true"><path d="M2 5h20v14H2z M2 5l10 8 10-8" fill="var(--brand-blue)"/><path d="M2 5l10 8 10-8" fill="none" stroke="#fff" stroke-width="2"/></svg>
        sleep@quorvana.com
      </li>
      <li>
        <svg viewBox="0 0 24 24" aria-hidden="true"><circle cx="12" cy="12" r="9.5" fill="none" stroke="var(--brand-blue)" stroke-width="2"/><path d="M2.5 12h19M12 2.5c3 3 3 16 0 19M12 2.5c-3 3-3 16 0 19" fill="none" stroke="var(--brand-blue)" stroke-width="1.6"/></svg>
        www.quorvana.com
      </li>
    </ul>
    <svg class="footer-band" viewBox="0 0 708 30" preserveAspectRatio="none" aria-hidden="true">
      <polygon points="0,7 338,7 318,30 0,30" fill="var(--band-grey)"/>
      <polygon points="383,0 708,0 708,30 345,30" fill="var(--brand-blue)"/>
    </svg>
  </section>
</main>
</body>
</html>
```